Residential & commercial landscaping company

Updated business cards for commercial and landscaping company. We would like to keep out logo, but just need a more updated business card.

```html
<!DOCTYPE html>
<html lang="en">
<head>
<meta charset="utf-8">
<title>Greenmere Business Card</title>
<link rel="stylesheet" href="https://fonts.googleapis.com/css2?family=Arimo:wght@400;700&family=Libre+Baskerville:wght@700&display=swap">
<style>
  :root {
    --stage: #2f2f2f;
    --card-white: #ffffff;
    --mist: #ececec;
    --leaf: #2fb52f;
    --leaf-bright: #4cc74a;
    --forest: #0f7f2a;
    --forest-deep: #0a6a24;
    --ink: #111111;
    --paper-text: #ffffff;
  }
  * { box-sizing: border-box; margin: 0; padding: 0; }
  html, body {
    width: 1200px; height: 866px; overflow: hidden;
    background: var(--stage);
  }
  .sheet {
    position: relative; width: 1200px; height: 866px;
    display: flex; flex-direction: column; align-items: center; justify-content: center;
    gap: 40px;
  }
  .card {
    position: relative; width: 680px; height: 389px; overflow: hidden;
    box-shadow: 0 10px 24px rgba(0,0,0,.45);
  }
  /* Front */
  .card-front { background: var(--card-white); }
  .card-front .canopy-wash {
    position: absolute; inset: 0;
    background: radial-gradient(ellipse 70% 60% at 30% 20%, var(--mist) 0%, rgba(236,236,236,.5) 45%, rgba(255,255,255,0) 75%);
  }
  .corner-accent { position: absolute; left: 0; top: 66px; width: 44px; height: 60px; }
  .contact {
    position: absolute; left: 48px; top: 78px;
    font-family: "Arimo", Arial, sans-serif; color: var(--ink);
  }
  .contact .person-name {
    font-family: "Libre Baskerville", Georgia, serif; font-weight: 700;
    font-size: 30px; color: var(--leaf); letter-spacing: .5px; line-height: 1.1;
  }
  .contact .person-role { font-size: 17px; margin: 4px 0 12px 2px; }
  .contact .line {
    display: flex; align-items: center; gap: 8px;
    font-size: 17px; line-height: 24px; letter-spacing: .3px;
  }
  .contact .line svg { width: 16px; height: 16px; flex: none; }
  .brand-front {
    position: absolute; right: 52px; top: 214px;
    display: flex; align-items: center; gap: 12px;
    font-family: "Arimo", Arial, sans-serif; font-weight: 700;
    font-size: 54px; color: var(--ink); letter-spacing: -1px;
  }
  .brand-front .brand-dot {
    width: 26px; height: 26px; background: var(--forest); border-radius: 50%;
  }
  /* Back */
  .card-back {
    background: linear-gradient(160deg, var(--forest-deep) 0%, var(--forest) 45%, var(--leaf-bright) 100%);
    display: flex; align-items: center; justify-content: center;
  }
  .card-back .canopy-wash {
    position: absolute; inset: 0;
    background: radial-gradient(ellipse 80% 70% at 50% 60%, rgba(0,80,20,.25), rgba(0,80,20,0) 70%);
  }
  .brand-back {
    position: relative;
    font-family: "Arimo", Arial, sans-serif; font-weight: 700;
    font-size: 76px; color: var(--paper-text); letter-spacing: -1px;
  }
</style>
</head>
<body>
<main class="sheet">
  <section class="card card-front">
    <div class="canopy-wash" role="img" aria-label="faint grey tree canopy silhouette"></div>
    <svg class="corner-accent" viewBox="0 0 44 60" aria-hidden="true">
      <polygon points="0,0 14,0 30,30 14,60 0,60" fill="var(--forest)"/>
      <polygon points="18,14 30,30 18,46 24,30" fill="var(--leaf)"/>
    </svg>
    <div class="contact">
      <p class="person-name">Daniel Hartwell Jr.</p>
      <p class="person-role">Project Manager</p>
      <p class="line">
        <svg viewBox="0 0 16 16" aria-hidden="true"><path d="M4 1.5l2.5 3-1.6 1.6c.8 1.9 2.2 3.3 4.1 4.1l1.6-1.6 3 2.5-1.6 2.6C7.5 13.7 2.3 8.5 1.4 3.1z" fill="var(--leaf)"/></svg>
        555-201-0148 ext.305
      </p>
      <p class="line">
        <svg viewBox="0 0 16 16" aria-hidden="true"><rect x="4" y="1.5" width="8" height="4" fill="var(--leaf)"/><rect x="1.5" y="6" width="13" height="6" rx="1" fill="var(--leaf)"/><rect x="4" y="10" width="8" height="4.5" fill="#fff" stroke="var(--leaf)" stroke-width="1.2"/></svg>
        555-304-7762
      </p>
      <p class="line">
        <svg viewBox="0 0 16 16" aria-hidden="true"><rect x="1" y="3.5" width="14" height="9" fill="var(--leaf)"/><path d="M1 3.5l7 5.5 7-5.5" fill="none" stroke="#fff" stroke-width="1.3"/></svg>
        dan@GreenmereLandscapes.com
      </p>
    </div>
    <div class="brand-front"><span class="brand-dot"></span>Greenmere</div>
  </section>

  <section class="card card-back">
    <div class="canopy-wash" role="img" aria-label="faint green tree canopy illustration"></div>
    <p class="brand-back">Greenmere</p>
  </section>
</main>
</body>
</html>
```